Updated website design needed for Radiology Group, Pinecrest Valley Imaging Partners

Clean, uncluttered, updated design needed for top regional Radiology Center. Focus on personal, patient oriented design, (not clinical). Should be simple and easy to navigate, with clear CTAs. Use blues, greens and photos of people in the Central Oregon outdoors.
Uncoded, PSD design only. 2 pages: Home page and one example interior page.
reference current site: http://www.pvipxq.com/
Sites they like:
http://www.hollowbrookscan.com/
http://www.mdlq.net/handler.cfm?event=practice,main
http://www.elmtidejoint.com/

Industry/Entity Type

Medical Imaging

Number of Pages Required

2 page

Font styles to use
Sans Serif

Requirements
Must have
• Personal and patient friendly.
• Lots of white space, clean and uncluttered. Clear CTAs, such as: Patient Bill Pay, Make an Appointment, Meet Our Doctors
• Use copy and contact information from the current site.
• Use outdoor images from Central Oregon, late Winter/ Spring (snow, light colors, spring green, for example)
• Include one example interior page, either Your Exam or Meet Our Doctors
Nice to have
• The client likes:
• Meet Our Doctors slider section, and big, easy to navigate Information Center on www.elmtidejoint.com
• The personal feel of the Your Exam section on www.hollowbrookscan.com
• Blues and Greens, outdoorsy imagery
Should not have
• The client does not like:
• complex drop down menus
• clinical feel
• Do not use lorum ipsum or dummy text.
• Do not use outdoor images from other regions. Do not use Summer (hot, poolside) or Fall (red/orange leaves) images.

```html
<!DOCTYPE html>
<html lang="en">
<head>
<meta charset="utf-8">
<title>Pinecrest Valley Imaging Partners</title>
<link rel="stylesheet" href="https://fonts.googleapis.com/css2?family=Roboto:wght@400;500;700&display=swap">
<style>
:root{
  --blue:#0f86c8;
  --blue-dark:#0a5f93;
  --green:#6abf0c;
  --green-dark:#4e9a06;
  --orange:#f39512;
  --orange-dark:#dd7a05;
  --ink:#2d2d2d;
  --text:#6b6b6b;
  --soft:#f3f3f3;
  --footer:#232528;
  --footer-line:#3a3d41;
  --white:#ffffff;
}
*{margin:0;padding:0;box-sizing:border-box}
html,body{width:1200px;height:2261px;overflow:hidden}
body{position:relative;background:var(--white);font-family:'Roboto',Arial,sans-serif;color:var(--ink)}
.abs{position:absolute}

/* header */
.brand{left:99px;top:21px;display:flex;align-items:center;gap:14px}
.brand-mark{width:60px;height:60px;background:var(--blue)}
.brand-name{font-size:22px;line-height:26px;font-weight:500;color:#3b3b6b;width:220px}
.contacts{right:100px;top:18px;text-align:right;font-size:13px;line-height:22px;color:#222;font-weight:500}

.nav{left:0;top:124px;width:1200px;height:83px;background:var(--blue);display:flex;align-items:center;padding-left:99px}
.nav a{color:var(--white);text-decoration:none;font-size:13px;margin-right:31px;text-transform:uppercase}
.nav a.current{color:#0b1c2c}

/* hero */
.hero{left:0;top:207px;width:1200px;height:672px;background:linear-gradient(180deg,#1b2534 0%,#2c3a4e 40%,#6d7a8c 75%,#98a3b2 100%)}
.hero-title{left:0;top:735px;width:1200px;text-align:center;color:var(--white);font-size:37px;font-weight:500;letter-spacing:.3px}
.hero-arrow{top:525px;width:38px;height:38px}

.cta{top:838px;height:73px;display:flex;color:var(--white);font-size:19px;font-weight:500;overflow:hidden}
.cta .label{flex:1;display:flex;align-items:center;padding-left:18px;white-space:nowrap}
.cta .icon{width:92px;flex:none;display:flex;align-items:center;justify-content:center}
.cta-pay{left:99px;width:302px;background:var(--blue)}
.cta-pay .label{padding-left:25px}
.cta-pay .icon{background:var(--blue-dark)}
.cta-appt{left:431px;width:327px;background:var(--green)}
.cta-appt .icon{background:var(--green-dark);width:84px}
.cta-docs{left:788px;width:312px;background:var(--orange)}
.cta-docs .icon{background:var(--orange-dark)}

/* welcome */
.welcome-title{left:0;top:952px;width:1200px;text-align:center;font-size:22px;font-weight:500;color:#333}
.welcome-text{left:190px;top:998px;width:820px;text-align:center;font-size:12px;line-height:20px;color:var(--text)}

.card{top:1097px;width:321px}
.card-photo{width:321px;height:204px;border:3px solid #e6e6e6}
.card-title{margin-top:26px;font-size:16px;font-weight:500;color:#111}
.card-text{margin-top:12px;font-size:11.5px;line-height:20px;color:var(--text);height:40px;text-align:justify}
.slider-chev{top:1140px;width:26px;height:104px}

.btn{display:flex;height:43px;width:133px;color:var(--white);font-size:11px;font-weight:500}
.btn .t{flex:1;background:var(--blue);display:flex;align-items:center;justify-content:center}
.btn .g{width:44px;background:var(--blue-dark);display:flex;align-items:center;justify-content:center}

/* feature */
.feature{left:0;top:1506px;width:1200px;height:401px;background:var(--soft)}
.video{left:99px;top:1558px;width:477px;height:290px;border:3px solid #e2e2e2;background:linear-gradient(180deg,#1f4a66 0%,#27506a 55%,#3d6b3e 100%)}
.video-bar{position:absolute;left:0;bottom:0;width:100%;height:22px;background:#222}
.feature-title{left:600px;top:1555px;width:500px;font-size:16.5px;line-height:23px;color:#333;font-weight:400}
.feature-text{left:600px;top:1620px;width:500px;font-size:11.5px;line-height:19.6px;color:var(--text);text-align:justify}

/* footer */
.footer{left:0;top:1907px;width:1200px;height:354px;background:var(--footer)}
.fcol{top:1945px;color:var(--white)}
.fcol h4{font-size:15px;font-weight:500;margin-bottom:14px}
.fcol li{list-style:none;font-size:12.5px;color:#d8d8d8;height:24px;display:flex;align-items:center;gap:12px}
.fcol li svg{flex:none}
.fdiv{top:1952px;width:1px;height:220px;background:var(--footer-line)}
.credit{left:0;top:2205px;width:1200px;text-align:center;font-size:11.5px;color:#d8d8d8}
</style>
</head>
<body>

<div class="abs brand">
  <div class="brand-mark"></div>
  <div class="brand-name">Pinecrest Valley Imaging Partners</div>
</div>
<div class="abs contacts">
  Main Line: (541) 555-0140<br>
  Scheduling: (541) 555-0142<br>
  Billing: (541) 555-0143<br>
  Medical Records: (541) 555-0144
</div>

<nav class="abs nav">
  <a class="current">Home</a><a>About Us</a><a>Our Services</a><a>For Patients</a><a>Our Physicians</a><a>For Physicians</a><a>PACS &amp; Documents</a><a>Appointments</a><a>Locations</a>
</nav>

<div class="abs hero" role="img" aria-label="Snowy groomed ski slope with a chairlift among pine trees at dusk"></div>
<svg class="abs hero-arrow" style="left:60px" viewBox="0 0 38 38"><circle cx="19" cy="19" r="17" fill="rgba(255,255,255,.15)" stroke="rgba(255,255,255,.6)" stroke-width="2"/><path d="M22 11l-8 8 8 8" fill="none" stroke="rgba(255,255,255,.75)" stroke-width="3"/></svg>
<svg class="abs hero-arrow" style="left:1101px" viewBox="0 0 38 38"><circle cx="19" cy="19" r="17" fill="rgba(255,255,255,.15)" stroke="rgba(255,255,255,.6)" stroke-width="2"/><path d="M16 11l8 8-8 8" fill="none" stroke="rgba(255,255,255,.75)" stroke-width="3"/></svg>
<div class="abs hero-title">PINECREST VALLEY IMAGING PARTNERS</div>

<div class="abs cta cta-pay"><div class="label">PATIENT BILL PAY</div><div class="icon">
  <svg width="46" height="34" viewBox="0 0 46 34"><rect x="6" y="4" width="34" height="22" rx="3" fill="none" stroke="#fff" stroke-width="3"/><rect x="6" y="10" width="34" height="4" fill="#fff"/></svg></div></div>
<div class="abs cta cta-appt"><div class="label">MAKE AN APPOINTMENT</div><div class="icon">
  <svg width="44" height="44" viewBox="0 0 44 44"><circle cx="22" cy="22" r="18" fill="none" stroke="#fff" stroke-width="3"/><path d="M14 13c2-2 4 0 5 2s0 3-1 4c1 3 3 5 6 6 1-1 2-2 4-1s4 3 2 5c-2 2-6 2-10-1s-8-8-8-11 1-3 2-4z" fill="#fff"/></svg></div></div>
<div class="abs cta cta-docs"><div class="label">MEET OUR DOCTORS</div><div class="icon">
  <svg width="40" height="44" viewBox="0 0 40 44"><circle cx="20" cy="13" r="9" fill="none" stroke="#fff" stroke-width="3"/><path d="M4 42c0-10 7-16 16-16s16 6 16 16z" fill="none" stroke="#fff" stroke-width="3"/><path d="M28 32h6M31 29v6" stroke="#fff" stroke-width="2.5"/></svg></div></div>

<h1 class="abs welcome-title">WELCOME TO PINECREST VALLEY IMAGING PARTNERS</h1>
<p class="abs welcome-text">Pinecrest Valley Imaging Partners is a diagnostic imaging corporation providing professional services to Central and Eastern Oregon hospitals and clinics as well as state-of-the-art services in its' own outpatient imaging center. PVIP was established by its' founder, Harold T. Wexbury, MD when he opened his Central Oregon practice in 1947.</p>

<svg class="abs slider-chev" style="left:64px" viewBox="0 0 26 104"><path d="M22 2L4 52l18 50" fill="none" stroke="#d4d4d4" stroke-width="2"/></svg>
<svg class="abs slider-chev" style="left:1110px" viewBox="0 0 26 104"><path d="M4 2l18 50L4 102" fill="none" stroke="#d4d4d4" stroke-width="2"/></svg>

<article class="abs card" style="left:99px">
  <div class="card-photo" role="img" aria-label="Rendered view inside the colon from a virtual colonoscopy" style="background:linear-gradient(135deg,#2a0f0c,#6e2a22 50%,#a8716a)"></div>
  <h3 class="card-title">Virtual Colonoscopy (VC),</h3>
  <p class="card-text">also referred to as CT colonography, is a safe exam used for colon polyp screening. VC technology creates a picture</p>
  <div class="btn" style="margin-top:42px"><span class="t">READ MORE</span><span class="g"><svg width="18" height="16" viewBox="0 0 18 16"><circle cx="6" cy="9" r="4" fill="none" stroke="#fff" stroke-width="2"/><circle cx="13.5" cy="4.5" r="2.5" fill="none" stroke="#fff" stroke-width="1.6"/></svg></span></div>
</article>
<article class="abs card" style="left:439px">
  <div class="card-photo" role="img" aria-label="Technologist preparing a patient for an MRI scanner" style="background:linear-gradient(135deg,#d8c98a,#bfb98c 45%,#6e8fb8)"></div>
  <h3 class="card-title">Magnetic Resonance Imaging (MRI)</h3>
  <p class="card-text">has three convenient locations Redmond (Juniper Way), PVIP on the eastside of Bend, and HDMC-Bend.</p>
  <div class="btn" style="margin-top:40px"><span class="t">READ MORE</span><span class="g"><svg width="18" height="16" viewBox="0 0 18 16"><circle cx="6" cy="9" r="4" fill="none" stroke="#fff" stroke-width="2"/><circle cx="13.5" cy="4.5" r="2.5" fill="none" stroke="#fff" stroke-width="1.6"/></svg></span></div>
</article>
<article class="abs card" style="left:779px">
  <div class="card-photo" role="img" aria-label="Patient standing at a digital mammography unit" style="background:linear-gradient(135deg,#e8ddd2,#c9b3a0 50%,#8aa8c4)"></div>
  <h3 class="card-title">Digital Mammography</h3>
  <p class="card-text">Every 2 minutes there's a new breast cancer diagnosis made. Spend 15 minutes getting your mammogram to help.</p>
  <div class="btn" style="margin-top:42px"><span class="t">READ MORE</span><span class="g"><svg width="18" height="16" viewBox="0 0 18 16"><circle cx="6" cy="9" r="4" fill="none" stroke="#fff" stroke-width="2"/><circle cx="13.5" cy="4.5" r="2.5" fill="none" stroke="#fff" stroke-width="1.6"/></svg></span></div>
</article>

<section class="abs feature"></section>
<div class="abs video" role="img" aria-label="Animated video about 3D mammography screening">
  <svg style="position:absolute;left:196px;top:96px" width="84" height="84" viewBox="0 0 84 84"><circle cx="42" cy="42" r="40" fill="rgba(255,255,255,.45)"/><path d="M33 26l26 16-26 16z" fill="#fff"/></svg>
  <div class="video-bar">
    <svg width="471" height="22" viewBox="0 0 471 22"><path d="M12 6l9 5-9 5z" fill="#fff"/><rect x="60" y="9" width="340" height="4" fill="#555"/><rect x="60" y="9" width="128" height="4" fill="var(--blue)"/><rect x="412" y="7" width="40" height="8" fill="#5a8fd0"/></svg>
  </div>
</div>
<h2 class="abs feature-title">3D Mammography is a revolutionary new screening and diagnostic tool designed for early breast cancer detection</h2>
<p class="abs feature-text">PVIP is staffed by fellowship trained physicians with expertise in major disciplines to include mammography, ultrasound, Magnetic Resonance Imaging, Computed Tomography, Positron Emission Tomography, interventional procedures, Nuclear Medicine and general procedures which include fluoroscopy, tomography, IVP's and radiographic procedures for head, chest, abdomen and extremity examinations. All technologists have advanced level training and certifications in modalities they specialize in. Each of our imaging modalities has either been granted National Imaging Accreditation Board accreditation or is in the process of doing so. This rigorous process provides a stamp of approval for the entire imaging process, including the equipment.</p>
<div class="abs btn" style="left:600px;top:1808px;height:41px"><span class="t">READ MORE</span><span class="g"><svg width="18" height="16" viewBox="0 0 18 16"><circle cx="6" cy="9" r="4" fill="none" stroke="#fff" stroke-width="2"/><circle cx="13.5" cy="4.5" r="2.5" fill="none" stroke="#fff" stroke-width="1.6"/></svg></span></div>

<footer class="abs footer"></footer>
<div class="abs fdiv" style="left:300px"></div>
<div class="abs fdiv" style="left:558px"></div>
<div class="abs fdiv" style="left:816px"></div>

<div class="abs fcol" style="left:99px"><h4>FOR PATIENTS</h4><ul>
  <li><svg width="12" height="8" viewBox="0 0 12 8"><path d="M0 4h10M7 1l3 3-3 3" fill="none" stroke="var(--blue)" stroke-width="1.5"/></svg>About Your Visit</li>
  <li><svg width="12" height="8" viewBox="0 0 12 8"><path d="M0 4h10M7 1l3 3-3 3" fill="none" stroke="var(--blue)" stroke-width="1.5"/></svg>Why Choose Us?</li>
  <li><svg width="12" height="8" viewBox="0 0 12 8"><path d="M0 4h10M7 1l3 3-3 3" fill="none" stroke="var(--blue)" stroke-width="1.5"/></svg>Patient Forms</li>
  <li><svg width="12" height="8" viewBox="0 0 12 8"><path d="M0 4h10M7 1l3 3-3 3" fill="none" stroke="var(--blue)" stroke-width="1.5"/></svg>Billing and Insurance</li>
  <li><svg width="12" height="8" viewBox="0 0 12 8"><path d="M0 4h10M7 1l3 3-3 3" fill="none" stroke="var(--blue)" stroke-width="1.5"/></svg>Locations and Maps</li>
  <li><svg width="12" height="8" viewBox="0 0 12 8"><path d="M0 4h10M7 1l3 3-3 3" fill="none" stroke="var(--blue)" stroke-width="1.5"/></svg>Appointments</li>
</ul></div>

<div class="abs fcol" style="left:369px"><h4>GENERAL</h4><ul>
  <li><svg width="12" height="8" viewBox="0 0 12 8"><path d="M0 4h10M7 1l3 3-3 3" fill="none" stroke="var(--blue)" stroke-width="1.5"/></svg>Home</li>
  <li><svg width="12" height="8" viewBox="0 0 12 8"><path d="M0 4h10M7 1l3 3-3 3" fill="none" stroke="var(--blue)" stroke-width="1.5"/></svg>About Us</li>
  <li><svg width="12" height="8" viewBox="0 0 12 8"><path d="M0 4h10M7 1l3 3-3 3" fill="none" stroke="var(--blue)" stroke-width="1.5"/></svg>Our Physicians</li>
  <li><svg width="12" height="8" viewBox="0 0 12 8"><path d="M0 4h10M7 1l3 3-3 3" fill="none" stroke="var(--blue)" stroke-width="1.5"/></svg>For Physicians</li>
  <li><svg width="12" height="8" viewBox="0 0 12 8"><path d="M0 4h10M7 1l3 3-3 3" fill="none" stroke="var(--blue)" stroke-width="1.5"/></svg>Disclaimer</li>
  <li><svg width="12" height="8" viewBox="0 0 12 8"><path d="M0 4h10M7 1l3 3-3 3" fill="none" stroke="var(--blue)" stroke-width="1.5"/></svg>HIPAA</li>
  <li><svg width="12" height="8" viewBox="0 0 12 8"><path d="M0 4h10M7 1l3 3-3 3" fill="none" stroke="var(--blue)" stroke-width="1.5"/></svg>Log-In</li>
</ul></div>

<div class="abs fcol" style="left:632px"><h4>QUICK LINKS</h4><ul>
  <li><svg width="12" height="8" viewBox="0 0 12 8"><path d="M0 4h10M7 1l3 3-3 3" fill="none" stroke="var(--blue)" stroke-width="1.5"/></svg>Our Services</li>
  <li><svg width="12" height="8" viewBox="0 0 12 8"><path d="M0 4h10M7 1l3 3-3 3" fill="none" stroke="var(--blue)" stroke-width="1.5"/></svg>Mammography</li>
  <li><svg width="12" height="8" viewBox="0 0 12 8"><path d="M0 4h10M7 1l3 3-3 3" fill="none" stroke="var(--blue)" stroke-width="1.5"/></svg>MRI</li>
  <li><svg width="12" height="8" viewBox="0 0 12 8"><path d="M0 4h10M7 1l3 3-3 3" fill="none" stroke="var(--blue)" stroke-width="1.5"/></svg>CT-64</li>
  <li><svg width="12" height="8" viewBox="0 0 12 8"><path d="M0 4h10M7 1l3 3-3 3" fill="none" stroke="var(--blue)" stroke-width="1.5"/></svg>X-Ray</li>
  <li><svg width="12" height="8" viewBox="0 0 12 8"><path d="M0 4h10M7 1l3 3-3 3" fill="none" stroke="var(--blue)" stroke-width="1.5"/></svg>Nuclear Medicine</li>
  <li><svg width="12" height="8" viewBox="0 0 12 8"><path d="M0 4h10M7 1l3 3-3 3" fill="none" stroke="var(--blue)" stroke-width="1.5"/></svg>PET</li>
  <li><svg width="12" height="8" viewBox="0 0 12 8"><path d="M0 4h10M7 1l3 3-3 3" fill="none" stroke="var(--blue)" stroke-width="1.5"/></svg>Ultrasound</li>
</ul></div>

<div class="abs fcol" style="left:880px"><h4>CONTACT US</h4><ul>
  <li><svg width="12" height="12" viewBox="0 0 12 12"><path d="M2 1c1-1 2 0 3 1s0 2-1 2c1 2 2 3 4 4 0-1 1-2 2-1s2 2 1 3c-1 1-4 1-6-1S0 3 2 1z" fill="var(--blue)"/></svg>(541) 555-0140 - Main Line</li>
  <li><svg width="12" height="12" viewBox="0 0 12 12"><path d="M2 1c1-1 2 0 3 1s0 2-1 2c1 2 2 3 4 4 0-1 1-2 2-1s2 2 1 3c-1 1-4 1-6-1S0 3 2 1z" fill="var(--blue)"/></svg>(541) 555-0142 - Scheduling</li>
  <li><svg width="12" height="12" viewBox="0 0 12 12"><path d="M2 1c1-1 2 0 3 1s0 2-1 2c1 2 2 3 4 4 0-1 1-2 2-1s2 2 1 3c-1 1-4 1-6-1S0 3 2 1z" fill="var(--blue)"/></svg>(541) 555-0143 - Billing</li>
  <li><svg width="12" height="12" viewBox="0 0 12 12"><path d="M2 1c1-1 2 0 3 1s0 2-1 2c1 2 2 3 4 4 0-1 1-2 2-1s2 2 1 3c-1 1-4 1-6-1S0 3 2 1z" fill="var(--blue)"/></svg>(541) 555-0144 - Medical Records</li>
</ul></div>

<p class="abs credit">Radiology Website Design | Medical Website Design by Brightfern Studio, Inc.</p>

</body>
</html>
```